Australian tool shop needs a label designed for a new product

we need a label designed for a new product (Trowel Mate) but since its new to the market we want the label to be based on the design of the top 2 existing brands so it is instantly familiar with the customer, attached a photo of the 2 different brands that it needs to look like

Target Market(s)

BRICKLAYERS/ BUILDERS

Industry/Entity Type

Building Product

Requirements
Must have
• MUST HAVE SIMULAR FEELS AS THE UPLOADED IMAGE AND FEEL FAMILIAR WITH THOSE BRANDS

```html
<!DOCTYPE html>
<html lang="en">
<head>
<meta charset="utf-8">
<title>Trowel Mate Label</title>
<link href="https://fonts.googleapis.com/css2?family=Anton&family=Comfortaa:wght@500;700&display=swap" rel="stylesheet">
<style>
  :root {
    --orange: #f47a23;
    --navy: #152d4a;
    --white: #ffffff;
    --badge-red: #d91f26;
    --badge-dark: #a8161c;
    --trim-red: #e3262d;
    --page: #ffffff;
  }
  * { box-sizing: border-box; margin: 0; padding: 0; }
  html, body {
    width: 720px; height: 1200px; overflow: hidden;
    background: var(--page);
  }
  .stage { position: relative; width: 720px; height: 1200px; }
  .label {
    position: absolute; left: 20px; top: 260px;
    width: 808px; height: 808px;
    transform: scale(0.8416); transform-origin: 0 0;
    background: var(--orange);
    border: 2px solid var(--trim-red);
    overflow: hidden;
    font-family: "Comfortaa", sans-serif;
    color: var(--white);
  }
  .label__split { position: absolute; inset: 0; width: 100%; height: 100%; }
  .title {
    position: absolute; left: 0; right: 10px; top: 50px;
    text-align: center;
    font-family: "Anton", sans-serif;
    font-size: 118px; line-height: 124px;
    letter-spacing: 1px; text-transform: uppercase;
  }
  .badge {
    position: absolute; left: 44px; top: 286px;
    width: 140px; height: 104px;
  }
  .badge svg { position: absolute; inset: 0; }
  .badge__text {
    position: absolute; inset: 0;
    display: flex; flex-direction: column; justify-content: center; align-items: center;
    font-size: 18px; font-weight: 500; line-height: 21px; letter-spacing: 0.5px;
  }
  .trowel-art {
    position: absolute; left: 150px; top: 390px;
    width: 530px; height: 62px;
    background: var(--white);
    border-radius: 40px 90px 90px 40px;
    transform: rotate(-10deg);
  }
  .copy { position: absolute; left: 82px; top: 548px; width: 500px; }
  .copy__lead { font-size: 15px; font-weight: 500; line-height: 18px; margin-bottom: 10px; }
  .copy__body { font-size: 11.5px; font-weight: 500; line-height: 13.5px; }
  .icons { position: absolute; left: 80px; top: 688px; display: flex; gap: 14px; }
  .icon {
    width: 82px; height: 82px; border-radius: 50%;
    border: 4px solid var(--white);
    display: flex; flex-direction: column; align-items: center; justify-content: center;
  }
  .icon--volume .icon__num { font-size: 30px; line-height: 26px; font-weight: 500; }
  .icon--volume .icon__unit { font-size: 17px; line-height: 20px; font-weight: 500; }
  .icon__art { width: 44px; height: 44px; border-radius: 50%; background: rgba(255,255,255,0.85); }
</style>
</head>
<body>
<div class="stage">
  <section class="label">
    <svg class="label__split" viewBox="0 0 808 808" preserveAspectRatio="none" aria-hidden="true">
      <polygon points="0,486 808,352 808,808 0,808" fill="var(--navy)"/>
    </svg>

    <h1 class="title">Trowel<br>Mate</h1>

    <div class="badge">
      <svg viewBox="0 0 140 104" aria-hidden="true">
        <defs>
          <radialGradient id="badgeFill" cx="40%" cy="35%" r="70%">
            <stop offset="0" stop-color="var(--badge-red)"/>
            <stop offset="1" stop-color="var(--badge-dark)"/>
          </radialGradient>
        </defs>
        <ellipse cx="70" cy="52" rx="69" ry="51" fill="url(#badgeFill)" stroke="var(--badge-dark)" stroke-width="2" stroke-dasharray="3 3"/>
      </svg>
      <div class="badge__text"><span>HIGH</span><span>QUALITY</span></div>
    </div>

    <div class="trowel-art" role="img" aria-label="White silhouette of a bricklayer's pointing trowel"></div>

    <div class="copy">
      <p class="copy__lead">All Natural Trowel Mate<br>is fine calcitic limestone in suspension</p>
      <p class="copy__body">Lorem ipsum dolor sit amet, consectetuer adipiscing elit, sed diam nonummy nibh euismod tincidunt ut laoreet dolore magna aliquam erat volutpat. Ut wisi enim ad minim Lorem ipsum dolor sit amet, consectetuer adipiscing elit, sed diam nonummy nibh euismod tincidunt ut laoreet dolore magna aliquam erat volutpat. Ut wisi enim ad minim</p>
    </div>

    <div class="icons">
      <div class="icon icon--volume"><span class="icon__num">2</span><span class="icon__unit">Liter</span></div>
      <div class="icon"><div class="icon__art" role="img" aria-label="Gloves icon"></div></div>
      <div class="icon"><div class="icon__art" role="img" aria-label="Work boots icon"></div></div>
      <div class="icon"><div class="icon__art" role="img" aria-label="Hand tools icon"></div></div>
    </div>
  </section>
</div>
</body>
</html>
```